Regenerative Medicine clinic needs PRP (Platelet Rich Plasma) marketing Tri-Fold Brochure

We are a physical medicine/Regnerative medicine clinic called 'Corevale Medical Group' out of Dallas, TX. We provide a Regenerative Medicine injection called 'Platelet Rich Plasma' or 'PRP' for patients with acute and chronic joint pain and joint conditions. We would like a brochure that outlines what PRP is, who is for, what it treats, and how it would benefit patients in a simplistic way. Pictures appreciated!

Target Market(s)

Older people with joint issues, and younger athletes

Industry/Entity Type

Medical, Regenerative Medicine

Font styles to use
Sans Serif

Colors
F0912C
F2A743
F7CA91
FBE8D2
FDF5EE

Requirements
Must have
• Logo and website and phone number - www.corevaleclinic.example, 214-555-0187

```html
<!DOCTYPE html>
<html lang="en">
<head>
<meta charset="UTF-8">
<title>Platelet Rich Plasma – Corevale Medical Group</title>
<link href="https://fonts.googleapis.com/css2?family=Poppins:wght@400;600;700&display=swap" rel="stylesheet">
<style>
  :root {
    --orange: #ec6f1a;
    --ink: #1f1f1f;
    --dark-panel: #2a2a2a;
    --paper: #ffffff;
    --backdrop: #d9d9d9;
    --white: #ffffff;
  }
  * { margin: 0; padding: 0; box-sizing: border-box; }
  html, body {
    width: 1141px; height: 1200px; overflow: hidden;
    background: var(--backdrop);
    font-family: "Poppins", sans-serif;
    color: var(--ink);
  }
  .flyer {
    position: absolute; left: 122px; top: 20px;
    width: 897px; height: 1160px;
    background: var(--paper); overflow: hidden;
  }
  .flyer-shapes { position: absolute; inset: 0; }
  .abs { position: absolute; white-space: nowrap; }
  .hero-title {
    left: 48px; top: 62px;
    font-weight: 700; font-size: 37px; line-height: 1;
    color: var(--white); letter-spacing: -0.8px;
  }
  .hero-sub {
    left: 48px; top: 106px;
    font-size: 22px; line-height: 28px; color: var(--white);
  }
  .hero-sub strong { font-weight: 700; }
  .section-heading { font-weight: 700; font-size: 25px; line-height: 32px; }
  .body-copy { font-size: 14.6px; line-height: 17.6px; }
  .what-heading { left: 47px; top: 233px; }
  .what-copy { left: 47px; top: 290px; }
  .who-card {
    left: 21px; top: 521px; width: 264px; height: 246px;
    background: var(--orange); border-radius: 20px; color: var(--white);
  }
  .who-card .section-heading { position: absolute; left: 27px; top: 8px; white-space: nowrap; }
  .who-card .body-copy { position: absolute; left: 27px; top: 62px; white-space: nowrap; }
  .benefits-heading { left: 385px; top: 650px; }
  .benefits-copy { left: 385px; top: 706px; }
  .about-heading { left: 45px; top: 805px; }
  .about-copy { left: 45px; top: 891px; }
  .brand {
    left: 45px; top: 1070px;
    display: flex; align-items: center; gap: 12px;
    font-size: 28px; font-weight: 400; color: var(--orange);
  }
  .brand-dot { width: 28px; height: 28px; border-radius: 50%; background: var(--orange); }
  .cta-title {
    left: 624px; top: 1012px;
    font-weight: 700; font-size: 19px; line-height: 23px; color: var(--white);
  }
  .cta-icon { left: 582px; top: 1021px; }
  .cta-contact {
    left: 582px; top: 1070px;
    font-size: 18px; line-height: 22px; color: var(--white);
  }
</style>
</head>
<body>
<main class="flyer">
  <svg class="flyer-shapes" width="897" height="1160" viewBox="0 0 897 1160">
    <defs>
      <linearGradient id="scene-tone" x1="0" y1="0" x2="1" y2="1">
        <stop offset="0" stop-color="#f4c9b0"/>
        <stop offset="0.5" stop-color="#7a74b8"/>
        <stop offset="1" stop-color="#5cc3de"/>
      </linearGradient>
      <radialGradient id="joint-tone" cx="0.58" cy="0.38" r="0.7">
        <stop offset="0" stop-color="#f06a4a"/>
        <stop offset="0.25" stop-color="#b0408a"/>
        <stop offset="0.6" stop-color="#2746b8"/>
        <stop offset="1" stop-color="#0b1a5c"/>
      </radialGradient>
    </defs>
    <rect class="injection-scene" x="360" y="230" width="500" height="391" rx="6" fill="url(#scene-tone)" opacity="0.5" role="img" aria-label="Illustration of a masked doctor giving an injection in a patient's upper arm"/>
    <path class="hero-banner" d="M0 39 Q300 10 615 97 L567 266 Q250 185 0 213 Z" fill="var(--orange)"/>
    <polygon class="banner-tail" points="609,156 726,194 653,245 671,338 489,281 491,257 572,274" fill="var(--orange)"/>
    <rect class="scene-rule" x="347" y="621" width="536" height="4" fill="var(--orange)"/>
    <path class="cta-panel" d="M897 844 L897 1160 L554 1160 L526 1052 Q516 1000 575 995 L640 990 Z" fill="var(--dark-panel)"/>
    <circle class="joint-image" cx="610" cy="900" r="103" fill="url(#joint-tone)" role="img" aria-label="X-ray style image of a glowing painful shoulder joint"/>
  </svg>

  <h1 class="abs hero-title">PLATELET RICH PLASMA</h1>
  <p class="abs hero-sub"><strong>A Regenerative Medicine injection</strong> To help<br>patients with acute and chronic joint pain<br>and joint conditions.</p>

  <h2 class="abs section-heading what-heading">What PRP is</h2>
  <p class="abs body-copy what-copy">Lorem ipsum dolor sit amet,<br>consectetuer adipiscing elit,<br>sed diam nonummy nibh<br>euismod tincidunt ut laoreet<br>dolore magna aliquam erat<br>volutpat. Ut wisi enim ad<br>minim veniam, quis nostrud<br>exerci tation ullamcorper<br>suscipit lobortis</p>

  <section class="abs who-card">
    <h2 class="section-heading">Who it is for</h2>
    <p class="body-copy">Lorem ipsum dolor sit amet,<br>consectetuer adipiscing elit,<br>sed diam nonummy nibh<br>euismod tincidunt ut laoreet<br>dolore magna aliquam erat<br>volutpat. Ut wisi enim ad<br>minim veniam, quis nostrud<br>exerci tation ullamcorper<br>suscipit lobortis</p>
  </section>

  <h2 class="abs section-heading benefits-heading">Benefits</h2>
  <p class="abs body-copy benefits-copy">Lorem ipsum dolor sit amet, consectetuer adipiscing elit, sed<br>diam nonummy nibh euismod tincidunt ut laoreet dolore<br>magna aliquam erat volutpat. Ut wisi enim ad minim veniam,<br>quis nostrud exerci tation ullamcorper suscipit lobortis</p>

  <h2 class="abs section-heading about-heading">About Corevale<br>Medical Group</h2>
  <p class="abs body-copy about-copy">Corevale Medical Group is conveniently located in<br>Uptown Dallas providing medical care, pain<br>management, physical rehabilitation, spinal<br>decompression therapy, massage therapy, knee<br>injections and ultrasound guided joint injections,<br>trigger point injections, medical weight loss and more.<br>We are your first stop for pain, arthritis, and injury care.</p>

  <div class="abs brand"><span class="brand-dot"></span><span>Corevale Medical Group</span></div>

  <svg class="abs cta-icon" width="34" height="30" viewBox="0 0 34 30" fill="none" stroke="var(--orange)" stroke-width="2" stroke-linejoin="round">
    <path d="M4 6 Q2 8 4 13 Q8 22 17 27 Q21 29 23 26 L24 24 L19 20 L16 22 Q10 18 8 12 L10 9 L6 4 Z"/>
    <rect x="17" y="3" width="15" height="11" rx="1"/>
    <path d="M17 4 L24.5 10 L32 4"/>
  </svg>
  <p class="abs cta-title">Request an<br>Appointment Today!</p>
  <p class="abs cta-contact">(214) 555-0187<br>www.corevaleclinic.example</p>
</main>
</body>
</html>
```